Business Card Design for Tarrabin Group - incorporates Tarrabin Steel & Kestrelon Engineering

The Group incorporates both the Tarrabin Steel & Kestrelon Engineering brands. The company is a steel fabrication business operating in Australia. We have workshops in Ridgeport, Calder & Merrow Falls.

```html
<!DOCTYPE html>
<html lang="en">
<head>
<meta charset="utf-8">
<title>Tarrabin Group Business Card</title>
<link href="https://fonts.googleapis.com/css2?family=Didact+Gothic&display=swap" rel="stylesheet">
<style>
  :root {
    --page: #e9e6e1;
    --steel-light: #f4f5f6;
    --steel-mid: #d3d6d9;
    --steel-dark: #a9adb2;
    --band-dark: #8e9398;
    --ink: #2b2d30;
    --ink-soft: #55595e;
    --rule: #6f7378;
    --brand-navy: #1f3a78;
    --brand-orange: #e9851f;
    --brand-yellow: #f1c232;
  }
  * { box-sizing: border-box; margin: 0; padding: 0; }
  html, body {
    width: 1200px; height: 800px; overflow: hidden;
    background: var(--page);
    font-family: "Didact Gothic", "Century Gothic", sans-serif;
    color: var(--ink);
  }
  .canvas {
    position: relative; width: 1200px; height: 800px;
    display: flex; align-items: center; justify-content: center; gap: 40px;
  }
  .card {
    position: relative; width: 540px; height: 330px;
    background: linear-gradient(160deg, var(--steel-light) 0%, var(--steel-mid) 45%, var(--steel-light) 70%, var(--steel-dark) 100%);
    box-shadow: 0 6px 18px rgba(0,0,0,0.22);
    overflow: hidden;
  }

  /* Back */
  .card-back .quote {
    position: absolute; top: 42px; left: 0; right: 0;
    text-align: center; font-size: 17px; line-height: 1.4; color: var(--ink-soft);
  }
  .card-back .band {
    position: absolute; top: 148px; left: 0; right: 0; height: 96px;
    background: radial-gradient(ellipse at 58% 50%, var(--steel-light) 0%, var(--steel-mid) 30%, var(--band-dark) 75%);
    border-top: 1px solid var(--rule); border-bottom: 1px solid var(--rule);
    display: flex; align-items: center; justify-content: space-between; padding: 0 36px;
  }
  .brand {
    display: flex; align-items: center; gap: 8px;
    font-size: 26px; color: var(--brand-navy); white-space: nowrap;
  }
  .brand .mark { width: 24px; height: 24px; border-radius: 50%; flex: none; }
  .brand-steel .mark { background: var(--brand-orange); }
  .brand-eng .mark { background: var(--brand-yellow); }
  .card-back .brand { color: #4a4e53; }
  .card-back .brand .mark { background: #7d8287; }

  /* Front */
  .card-front .top-rule {
    position: absolute; top: 74px; left: 24px; right: 24px; border-top: 1px solid var(--rule);
  }
  .card-front .brand-eng { position: absolute; top: 28px; right: 40px; font-size: 22px; }
  .card-front .brand-eng .mark { width: 20px; height: 20px; }
  .card-front .headline {
    position: absolute; top: 96px; left: 24px; right: 24px;
    display: flex; align-items: center; gap: 18px;
  }
  .card-front .brand-steel { font-size: 22px; }
  .card-front .brand-steel .mark { width: 22px; height: 22px; }
  .card-front .offices { font-size: 14px; color: var(--ink); white-space: nowrap; }
  .card-front .mid-rule {
    position: absolute; top: 144px; left: 24px; right: 24px; border-top: 1px solid var(--rule);
  }
  .column {
    position: absolute; font-size: 12px; line-height: 1.65; color: var(--ink-soft);
    white-space: nowrap;
  }
  .contact { top: 168px; left: 70px; padding-left: 14px; border-left: 1px solid var(--rule); height: 128px; }
  .contact .name { font-size: 18px; color: var(--ink); }
  .contact .role { margin-bottom: 20px; }
  .office { top: 168px; left: 300px; padding-left: 14px; border-left: 1px solid var(--rule); height: 104px; }
  .office .label { font-size: 14px; color: var(--ink); }
</style>
</head>
<body>
<main class="canvas">

  <section class="card card-back" aria-label="Card back">
    <p class="quote">"What matters most to our business,<br>Our Clients, Our Team and Our Good Name"</p>
    <div class="band">
      <div class="brand brand-steel"><span class="mark"></span>Tarrabin Steel</div>
      <div class="brand brand-eng"><span class="mark"></span>Kestrelon</div>
    </div>
  </section>

  <section class="card card-front" aria-label="Card front">
    <div class="brand brand-eng"><span class="mark"></span>Kestrelon</div>
    <div class="top-rule"></div>
    <div class="headline">
      <div class="brand brand-steel"><span class="mark"></span>Tarrabin Steel</div>
      <p class="offices">Offices in Ridgeport, Calder &amp; Merrow Falls</p>
    </div>
    <div class="mid-rule"></div>
    <div class="column contact">
      <p class="name">Daniel Hart</p>
      <p class="role">General Manager</p>
      <p>Mobile No. +61 412 508 337</p>
      <p>Email: d.hart@tarrabinsteel.com</p>
    </div>
    <div class="column office">
      <p class="label">Head Office</p>
      <p>118 Bowen Road, Tarrabin Qld 4921</p>
      <p>PO Box 207, Tarrabin Qld 4921</p>
      <p>Ph No. +61 7 4700 1234</p>
      <p>Fax No. +61 7 4700 1235</p>
    </div>
  </section>

</main>
</body>
</html>
```